Clearvane glass & hardware manufacturer

Need a SEO friendly, modern & professional looking website. We are selling all kinds of glass & accessories ( Glass/ Mirror/ splash back/ pool fence/ balustrade/ hardware...we are specialised on some special glass, like curve glass,tinted glass thermal & accoustic glass...) It should has simple & crisp feeling like a glass. It must be fully functional with product display and online ordering. Please see attached confirmed logo design(Blue & white). Make sure the theme color match its feel.

Target Market(s)

Architect and designer, Builder, & Developer

Industry/Entity Type

Manufacturer

Coding

Coded - Design and coding required

Font styles to use
Serif
Sans Serif

Colors

Designer to choose colors to be used in the design.

Requirements
Must have
• Glass & hardware theme and our logo
• Here are some competitor's website for reference. (Borrow ideas but not copy : )
• 1.https://www.lumaro.com.au/about
• 2.http://www.brightpanedirect.com.au/
• 3.http://www.tvk.com.au/
• 4.http://www.oakridgefittings.com.au/
Nice to have
• Some transparent or semi transparent effects to make the website like a glass
Should not have
• No limitation for your imagination

```html
<!DOCTYPE html>
<html lang="en">
<head>
<meta charset="utf-8">
<title>Clearvane – Glass &amp; Hardware</title>
<link rel="stylesheet" href="https://fonts.googleapis.com/css2?family=Open+Sans:wght@400;600;700&family=Open+Sans+Condensed:wght@700&family=Nunito+Sans:wght@700;800&display=swap">
<style>
  :root {
    --frame: #e6e6e6;
    --page: #ffffff;
    --brand: #29a8df;
    --brand-dark: #1d6fb8;
    --ink: #333333;
    --muted: #555555;
    --soft-band: #f3f3f3;
    --field-line: #c9c9c9;
    --field-bg: #fafafa;
    --button: #3a3968;
    --rule: #cfcfcf;
  }
  * { box-sizing: border-box; margin: 0; padding: 0; }
  html, body { width: 850px; height: 1200px; overflow: hidden; }
  body { background: var(--frame); font-family: "Open Sans", Arial, sans-serif; color: var(--ink); position: relative; }
  .page { position: absolute; left: 10px; top: 10px; width: 830px; height: 1180px; background: var(--page); }

  /* header */
  .site-header { position: absolute; left: 0; top: 0; width: 830px; height: 91px; }
  .brand { position: absolute; left: 44px; top: 12px; display: flex; align-items: center; gap: 10px; }
  .brand-mark { width: 42px; height: 42px; background: var(--brand); }
  .brand-name { font-family: "Nunito Sans", sans-serif; font-weight: 800; font-size: 30px; letter-spacing: 1px; color: var(--brand-dark); text-transform: uppercase; }
  .info-bar { position: absolute; left: 463px; top: 0; width: 350px; height: 26px; }
  .info-bar svg { position: absolute; left: 0; top: 0; }
  .info-text { position: absolute; left: 60px; top: 5px; font-family: "Open Sans", sans-serif; font-weight: 700; font-size: 11px; color: #fff; white-space: nowrap; }
  .phone-icon { position: absolute; left: 38px; top: 4px; }
  .social { position: absolute; left: 258px; top: 4px; display: flex; gap: 3px; }
  .social span { width: 16px; height: 16px; border: 1.3px solid #fff; border-radius: 50%; display: block; }
  .main-nav { position: absolute; top: 57px; left: 545px; display: flex; align-items: center; font-family: "Open Sans Condensed", "Open Sans", sans-serif; font-weight: 700; font-size: 12.5px; color: #111; text-transform: uppercase; }
  .main-nav a { color: inherit; text-decoration: none; margin-right: 14px; padding: 6px 0 4px; }
  .main-nav a.current { border-bottom: 3px solid var(--brand-dark); }
  .main-nav a.cta { background: var(--brand); color: #fff; padding: 4px 8px; border-radius: 2px; margin-right: 0; margin-left: -2px; }

  /* hero */
  .hero { position: absolute; left: 0; top: 91px; width: 830px; height: 393px;
    background: linear-gradient(160deg, #c7d9ee 0%, #e9eff7 35%, #8ea8c4 60%, #4e6d8e 80%, #f4f6f9 100%); }
  .hero-shadow { position: absolute; left: 30px; top: 484px; width: 780px; height: 14px;
    background: radial-gradient(ellipse at top, rgba(0,0,0,.22), rgba(0,0,0,0) 70%); }

  /* intro */
  .section-title { position: absolute; left: 0; width: 830px; display: flex; justify-content: center; align-items: center; gap: 14px; font-family: "Nunito Sans", sans-serif; font-weight: 800; }
  .section-title::before, .section-title::after { content: ""; height: 1px; background: var(--rule); }
  .intro-title { top: 525px; font-size: 17px; color: var(--brand); }
  .intro-title::before, .intro-title::after { width: 66px; }
  .intro-text { position: absolute; left: 50px; top: 577px; width: 730px; text-align: center; font-size: 9.2px; line-height: 14px; color: var(--muted); }

  /* contact */
  .contact { position: absolute; left: 0; top: 686px; width: 830px; height: 332px; background: var(--soft-band); }
  .contact-title { top: 38px; font-size: 17px; color: #222; }
  .contact-title::before, .contact-title::after { width: 66px; }
  .contact-title em { font-style: normal; color: #5f9bd6; }
  .field { position: absolute; height: 33px; border: 1.5px solid var(--field-line); border-radius: 4px; background: var(--field-bg); font-size: 11px; font-weight: 700; color: #333; padding: 8px 11px; }
  .field-name { left: 71px; top: 102px; width: 223px; }
  .field-email { left: 303px; top: 102px; width: 223px; }
  .field-subject { left: 535px; top: 102px; width: 223px; }
  .field-message { left: 71px; top: 144px; width: 687px; height: 95px; }
  .send-button { position: absolute; left: 348px; top: 249px; width: 134px; height: 30px; background: var(--button); color: #fff; border-radius: 4px; font-family: "Open Sans", sans-serif; font-weight: 700; font-size: 11px; display: flex; align-items: center; justify-content: center; letter-spacing: .2px; }

  /* footer */
  .footer-tab { position: absolute; left: 280px; top: 993px; }
  .footer-brand { position: absolute; left: 0; top: 1028px; width: 830px; display: flex; justify-content: center; align-items: center; gap: 10px; }
  .footer-brand .brand-mark { width: 40px; height: 40px; }
  .footer-line { position: absolute; left: 0; top: 1147px; width: 830px; height: 1px; background: #dcdcdc; }
  .copyright { position: absolute; left: 0; top: 1158px; width: 830px; text-align: center; font-size: 8.5px; font-weight: 700; color: #333; }
</style>
</head>
<body>
<div class="page">
  <header class="site-header">
    <div class="brand">
      <span class="brand-mark"></span>
      <span class="brand-name">Clearvane</span>
    </div>
    <div class="info-bar">
      <svg width="350" height="26" viewBox="0 0 350 26"><polygon points="0,0 350,0 326,26 24,26" fill="#29a8df"/></svg>
      <svg class="phone-icon" width="16" height="16" viewBox="0 0 16 16">
        <circle cx="8" cy="8" r="7" fill="none" stroke="#fff" stroke-width="1.3"/>
        <path d="M5.5 4.5 L7 4.5 L7.5 6.5 L6.6 7.2 Q7.6 9 8.8 9.5 L9.5 8.6 L11.5 9.1 L11.5 10.6 Q8.5 11 6.4 8.6 Q4.8 6.6 5.5 4.5 Z" fill="#fff"/>
      </svg>
      <span class="info-text">FOR INFORMATION : 1800 555 0142</span>
      <div class="social"><span></span><span></span><span></span></div>
    </div>
    <nav class="main-nav">
      <a class="current" href="#">Home</a>
      <a href="#">About</a>
      <a href="#">Services</a>
      <a href="#">News</a>
      <a class="cta" href="#">Contact Us</a>
    </nav>
  </header>

  <div class="hero" role="img" aria-label="Photo looking up at the glass corner of a modern building against a bright blue sky"></div>
  <div class="hero-shadow"></div>

  <h2 class="section-title intro-title">Clearvane - Glass &amp; Hardware</h2>
  <p class="intro-text">Lorem ipsum dolor sit amet, consectetuer adipiscing elit, sed diam nonummy nibh euismod tincidunt ut laoreet dolore magna aliquam erat volutpat. Ut wisi enim ad minim veniam, quis nostrud exerci tation ullamcorper suscipit lobortis nisl ut aliquip ex ea commodo consequat. Duis autem vel eum iriure dolor in hendrerit in vulputate velit esse molestie consequat, vel illum dolore eu feugiat nulla facilisis at vero eros et accumsan et iusto odio dignissim qui blandit praesent luptatum zzril delenit augue duis dolore te feugait nulla facilisi. Nam liber tempor cum soluta nobis eleifend option congue nihil imperdiet doming id quod mazim placerat facer possim assum. Typi non habent claritatem insitam; est usus legentis in iis qui facit eorum claritatem. Investigationes demonstraverunt lectores legere me lius quod ii legunt saepius.</p>

  <section class="contact">
    <h2 class="section-title contact-title"><span>Contact us! <em>Complete the form below to get started...</em></span></h2>
    <div class="field field-name">Your Name</div>
    <div class="field field-email">Your Email</div>
    <div class="field field-subject">Your Subject</div>
    <div class="field field-message">Message</div>
    <div class="send-button">SEND YOUR MESSAGE</div>
  </section>

  <svg class="footer-tab" width="276" height="36" viewBox="0 0 276 36">
    <path d="M0 36 L14 6 Q17 0 24 0 L252 0 Q259 0 262 6 L276 36 Z" fill="#ffffff"/>
  </svg>
  <div class="footer-brand">
    <span class="brand-mark"></span>
    <span class="brand-name">Clearvane</span>
  </div>
  <div class="footer-line"></div>
  <p class="copyright">© 2018 CLEARVANE I ALL RIGHTS RESERVED</p>
</div>
</body>
</html>
```